Where Quiet Rivers Carry Us

I have a previously designed book cover, and although I am mostly happy with it, I do not care for the photo on the cover of the book. I would like to keep the fonts and scrollwork on the current book cover (the brown outer edge is optional).
I prefer a Christian focus with a soft, gentle, grieving, trusting feeling of a mother as God leads without the typical religious symbols (ie: huge hands, overwhelming crosses, Heaven opening). Softly toned or small Christian icons would be acceptable.
The book dimensions are 5.5 X 8.5 and the spine is 1/2" thick.
Original book cover is here: http://wherequietriverscarryus.pinebrookpages.net/p/free-books.html
Back cover book description (two photos and the logo for the back cover can be found below) :
For I am the Lord your God who takes hold of your right hand and says to you, "Do not fear, I will help you." Isaiah 41:13
One day you were here, Colby, the next you were at the throne of God. How I long to know what heaven is like so I can envision where you are. Are you talking to Gideon about the battles of old? Are you asking Paul about the stonings, the scales, and the shipwrecks? Or are you still just standing in awe of the God and Savior that your mother could never have come close to describing to you? How I long to stand in awe with you, praising the God who gives and takes away. Just like I told you all those times when you were here with us, "If you go first, I'll see you when I get there, my son." Love you, Mom
On Friday, February 18, 2011, God did the unthinkable in our lives: He chose to take our 12-year-old son, Colby, home to heaven in a skiing accident. It is only considered the unthinkable because our plans are not God's plans and our ways are not God's ways. Follow along on my journey through the valley of the shadow of death as my Savior, Jesus Christ, leads me.
(Author info)
Janna L. Voskuilen lives on a small farm in northern Wisconsin with her husband, Dale, and their children. Experiencing the tragic death of her son has caused her to draw closer to God as He leads her down an unexpected path to know Him better.
I have updated the back cover details to include the exact words for the back cover as well as two photos and a logo. Thank you, designers, for sharing your creativity!
Reason: Still looking for the perfect book cover!
Reason: Still looking for the perfect design!
Working on final revisions!

```html
<!DOCTYPE html>
<html lang="en">
<head>
<meta charset="utf-8">
<title>Where Quiet Rivers Carry Us — Book Cover</title>
<link rel="stylesheet" href="https://fonts.googleapis.com/css2?family=Crimson+Text:ital,wght@0,400;0,600;1,400&family=Parisienne&display=swap">
<style>
  :root {
    --stage: #0d3f86;
    --parchment-light: #f3d79a;
    --parchment: #e7bd72;
    --parchment-dark: #c98f45;
    --spine-red: #a3151d;
    --deep-red: #8e1016;
    --verse-red: #9b1a1f;
    --ink: #3a2414;
    --gold: #e6c47a;
    --gold-soft: #d9b46a;
    --panel-black: #0b0705;
    --frame-red: #a4141b;
    --script: "Parisienne", cursive;
    --serif: "Crimson Text", Georgia, serif;
  }
  * { box-sizing: border-box; margin: 0; padding: 0; }
  html, body { width: 1200px; height: 845px; overflow: hidden; }
  body {
    background: radial-gradient(ellipse at 50% 45%, #1f8fd8 0%, #1160b3 45%, var(--stage) 100%);
    position: relative;
  }
  .book-spread {
    position: absolute;
    left: 85px; top: 42px;
    width: 1029px; height: 760px;
    display: flex;
    box-shadow: 0 12px 30px rgba(0,0,0,.35);
  }
  .parchment {
    background:
      radial-gradient(ellipse at 50% 45%, var(--parchment-light) 0%, var(--parchment) 60%, var(--parchment-dark) 100%);
  }

  /* Back cover */
  .back-cover { width: 492px; height: 760px; position: relative; }
  .back-cover .verse {
    position: absolute; left: 30px; right: 30px; top: 46px;
    font-family: var(--script); color: var(--verse-red);
    font-size: 27px; line-height: 32px; text-align: center;
  }
  .back-cover .verse .reference { display: block; text-align: right; padding-right: 40px; }
  .back-cover .blurb {
    position: absolute; left: 40px; right: 40px; top: 200px;
    font-family: var(--serif); font-style: italic; color: var(--ink);
    font-size: 13.6px; line-height: 19.5px; text-align: justify;
  }
  .back-cover .blurb p + p { margin-top: 10px; }
  .back-cover .family-photos {
    position: absolute; left: 40px; top: 548px; display: flex; gap: 12px;
  }
  .family-photos .photo {
    width: 64px; height: 84px; border: 2px solid #5a3a22;
    background: linear-gradient(160deg, #b59a7a 0%, #7d6249 55%, #4d3a2a 100%);
  }
  .back-cover .publisher-mark {
    position: absolute; right: 44px; top: 572px;
    width: 118px; height: 52px;
    background: #eadbc0; border: 1px solid #6a5640;
    display: flex; align-items: center; justify-content: center; gap: 6px;
    font-family: var(--serif); font-weight: 600; color: #1d1712;
    font-size: 12.5px; line-height: 14px; text-align: center;
  }
  .publisher-mark .mark-square { width: 8px; height: 8px; background: #1d1712; flex: none; }
  .back-cover .author-band {
    position: absolute; left: 26px; right: 26px; top: 640px; height: 72px;
    background: var(--deep-red);
    padding: 10px 14px;
    font-family: var(--serif); font-style: italic; color: var(--gold);
    font-size: 12.6px; line-height: 17px;
  }

  /* Spine */
  .spine {
    width: 45px; height: 760px; position: relative;
    background: linear-gradient(90deg, #7e0d13 0%, var(--spine-red) 30%, #b51c24 55%, var(--spine-red) 80%, #7e0d13 100%);
  }
  .spine .spine-text {
    position: absolute; left: 50%; top: 50%;
    width: 700px; transform: translate(-50%, -50%) rotate(90deg);
    display: flex; justify-content: space-between; align-items: center;
    font-family: var(--script); color: var(--gold-soft);
  }
  .spine .spine-title { font-size: 22px; margin-left: 40px; }
  .spine .spine-author { font-size: 18px; margin-right: 10px; }

  /* Front cover */
  .front-cover { width: 492px; height: 760px; position: relative; }
  .front-cover .photo-panel {
    position: absolute; left: 22px; top: 24px; right: 18px; bottom: 30px;
    background: var(--panel-black);
    border: 2px solid #2a0b0b;
  }
  .photo-panel .inner-frame {
    position: absolute; inset: 8px; border: 1.5px solid var(--frame-red);
  }
  .photo-panel .inner-frame::after {
    content: ""; position: absolute; inset: 5px; border: 1px solid var(--frame-red); opacity: .8;
  }
  .photo-panel .cover-art {
    position: absolute; left: 40px; right: 40px; top: 150px; bottom: 90px;
    background: radial-gradient(ellipse at 50% 55%, #fff6d6 0%, #f0c873 14%, #6a4a20 38%, #1a120b 65%, var(--panel-black) 100%);
  }
  .photo-panel .title {
    position: absolute; left: 0; right: 0; top: 50px;
    font-family: var(--script); color: var(--gold);
    font-size: 40px; line-height: 48px; text-align: center; font-weight: 400;
  }
  .photo-panel .author {
    position: absolute; left: 0; right: 0; bottom: 22px;
    font-family: var(--script); color: #efe3c6;
    font-size: 22px; text-align: center;
  }
  .scrollwork { position: absolute; }
  .scrollwork.top-right {
    right: 18px; top: 24px; width: 90px; height: 70px;
    background: radial-gradient(ellipse at 70% 30%, rgba(120,110,100,.55) 0%, rgba(60,55,50,0) 70%);
  }
  .scrollwork.bottom-left {
    left: 4px; bottom: 10px; width: 110px; height: 90px;
    background: radial-gradient(ellipse at 35% 65%, rgba(90,80,70,.5) 0%, rgba(90,80,70,0) 70%);
  }
  .scrollwork.corner-top {
    right: 0; top: 0; width: 70px; height: 40px;
    background: radial-gradient(ellipse at 80% 20%, rgba(150,60,20,.45) 0%, rgba(150,60,20,0) 70%);
  }
  .scrollwork.back-corner {
    left: 0; top: 0; width: 60px; height: 30px;
    background: radial-gradient(ellipse at 20% 20%, rgba(150,60,20,.4) 0%, rgba(150,60,20,0) 70%);
  }
</style>
</head>
<body>
  <main class="book-spread">
    <section class="back-cover parchment">
      <div class="scrollwork back-corner" role="img" aria-label="Small brown scrollwork flourish in the corner"></div>
      <blockquote class="verse">
        For I am the Lord your God who takes hold of your right hand and says to you, “Do not fear, I will help you.”
        <cite class="reference">Isaiah 41:13</cite>
      </blockquote>
      <div class="blurb">
        <p>One day you were here, Colby, the next you were at the throne of God. How I long to know what heaven is like so I can envision where you are. Are you talking to Gideon about the battles of old? Are you asking Paul about the stonings, the scales, and the shipwrecks? Or are you still just standing in awe of the God and Savior that your mother could never have come close to describing to you? How I long to stand in awe with you, praising the God who gives and takes away. Just like I told you all those times when you were here with us, “If you go first, I’ll see you when I get there, my son.” Love you, Mom</p>
        <p>On Friday, February 18, 2011, God did the unthinkable in our lives: He chose to take our 12-year-old son, Colby, home to heaven in a skiing accident. It is only considered the unthinkable because our plans are not God’s plans and our ways are not God’s ways. Follow along on my journey through the valley of the shadow of death as my Savior, Jesus Christ, leads me.</p>
      </div>
      <div class="family-photos">
        <div class="photo" role="img" aria-label="Sepia photo of the author"></div>
        <div class="photo" role="img" aria-label="Sepia photo of the author's son Colby"></div>
      </div>
      <div class="publisher-mark"><span class="mark-square"></span><span>Stillwater Hope Press</span></div>
      <p class="author-band">Janna L. Voskuilen lives on a small farm in northern Wisconsin with her husband, Dale, and their children. Experiencing the tragic death of her son has caused her to draw closer to God as He leads her down an unexpected path to know Him better.</p>
    </section>

    <section class="spine">
      <div class="spine-text">
        <span class="spine-title">Where Quiet Rivers Carry Us</span>
        <span class="spine-author">Janna L. Voskuilen</span>
      </div>
    </section>

    <section class="front-cover parchment">
      <div class="scrollwork corner-top" role="img" aria-label="Brown scrollwork flourish in the top corner"></div>
      <div class="photo-panel">
        <div class="inner-frame"></div>
        <div class="cover-art" role="img" aria-label="Photo of a glowing cross of light in a dark room"></div>
        <h1 class="title">Where Quiet Rivers<br>Carry Us</h1>
        <p class="author">Janna L. Voskuilen</p>
      </div>
      <div class="scrollwork top-right" role="img" aria-label="Grey scrollwork ornament in the panel corner"></div>
      <div class="scrollwork bottom-left" role="img" aria-label="Grey scrollwork ornament in the lower corner"></div>
    </section>
  </main>
</body>
</html>
```